PEACFUL ACUPUNCTURE PRACTITIONER NEEDS A NEW COAT

I need a new design for an exiting website http://stillwillowneedlework.example/ for a acupuncturist. This will be a minimalism design with lots and lots of white space. Home page and one interior page. Please keep the feeling of calm and peaceful serenity. For Color scheme: https://www.harborfernclinic.example/fertility. The bottom part of the home page with sections and links to the service pages: https://mossgatewellness.example/. The client likes this the best: http://qlhealing.example/. I'm attaching the logo and content pages.

Target Market(s)

Women

Industry/Entity Type

Wellness, health, wellbeing, meditation

Number of Pages Required

2 page

Font styles to use
Sans Serif
Decorative

Colors

Designer to choose colors to be used in the design.

Requirements
Must have
Nice to have
• Follow new website drafts and links
Should not have
• Busy with bright colors. No poping

```html
<!DOCTYPE html>
<html lang="en">
<head>
<meta charset="utf-8">
<title>Still Willow Acupuncture</title>
<link rel="stylesheet" href="https://fonts.googleapis.com/css2?family=Marcellus&family=Quicksand:wght@400;500;600&display=swap">
<style>
:root{
  --ink:#3a3536;
  --muted:#6f6868;
  --rose:#b88a8f;
  --rose-soft:#e8c9cf;
  --cream:#fdf1df;
  --blush:#faeaf1;
  --paper:#fdfcfc;
  --disc:#f4f2f2;
  --line:#e6e2e2;
}
*{margin:0;padding:0;box-sizing:border-box}
html,body{width:1200px;height:2680px;overflow:hidden}
body{position:relative;background:var(--paper);font-family:"Quicksand",sans-serif;color:var(--ink)}
.abs{position:absolute}

/* header */
.nav-rule{position:absolute;height:1px;background:var(--line)}
.nav-link{position:absolute;top:55px;font-size:10px;letter-spacing:2px;text-transform:uppercase;color:var(--ink);transform:translateX(-50%)}
.nav-link.is-active{color:var(--rose)}
.nav-link.is-active::after{content:"";position:absolute;left:50%;top:27px;width:36px;height:2px;background:var(--rose);transform:translateX(-50%)}
.nav-caret{position:absolute;top:86px;width:5px;height:5px;border-right:1px solid var(--ink);border-bottom:1px solid var(--ink);transform:translateX(-50%) rotate(45deg)}
.brand{position:absolute;left:600px;transform:translateX(-50%);text-align:center}
.brand-mark{width:50px;height:50px;border-radius:50%;background:var(--rose-soft);margin:0 auto 6px}
.brand-name{font-family:"Marcellus",serif;font-size:23px;color:var(--ink);line-height:1;white-space:nowrap}
.brand-sub{font-family:"Marcellus",serif;font-size:11px;letter-spacing:4px;color:var(--ink);margin-top:3px;text-transform:uppercase}

/* hero */
.hero-photo{position:absolute;left:10px;top:127px;width:1180px;height:598px;background:linear-gradient(100deg,#6d6f60 0%,#7d7c6b 35%,#b99483 55%,#d9b4a0 75%,#cfa28d 100%)}
.philosophy{position:absolute;left:227px;top:532px;width:746px;height:223px;background:var(--cream);text-align:center}
.philosophy h1{font-family:"Marcellus",serif;font-weight:400;font-size:38px;letter-spacing:2px;margin-top:42px}
.philosophy p{font-size:11px;line-height:18.5px;color:var(--muted);width:560px;margin:26px auto 0}
.btn{position:absolute;height:38px;background:var(--rose);color:#fff;font-size:8.5px;font-weight:600;letter-spacing:3.5px;text-transform:uppercase;display:flex;align-items:center;justify-content:center}

/* focus */
.section-title{position:absolute;font-family:"Marcellus",serif;font-weight:400;font-size:40px;letter-spacing:2px;color:var(--ink)}
.title-rule{position:absolute;height:1px;background:var(--rose-soft)}
.focus-item{position:absolute;top:962px;width:240px;text-align:center}
.focus-num{position:absolute;top:4px;right:-18px;font-family:"Marcellus",serif;font-size:54px;color:#f8f0f0}
.focus-disc{position:relative;width:220px;height:220px;border-radius:50%;background:var(--disc);margin:0 auto;overflow:hidden}
.focus-art{position:absolute;left:50%;top:50%;width:120px;height:120px;transform:translate(-50%,-50%);border-radius:50%}
.focus-item h3{font-weight:500;font-size:16.5px;line-height:23px;margin-top:25px}
.focus-item p{font-size:10.5px;line-height:17.5px;color:var(--muted);width:192px;margin:18px auto 0}
.focus-go{position:absolute;top:1453px;width:40px;height:40px;border-radius:50%;background:var(--rose);display:flex;align-items:center;justify-content:center}

/* contact */
.contact{position:absolute;left:0;top:1593px;width:1200px;height:627px;background:var(--blush)}
.contact-lead{position:absolute;left:125px;top:1758px;font-size:11px;line-height:19px;color:var(--muted);width:530px}
.phone{position:absolute;left:883px;top:1760px;display:flex;align-items:center;gap:16px}
.phone-icon{width:54px;height:54px;border-radius:50%;background:var(--rose);border:5px solid #f0d7de;display:flex;align-items:center;justify-content:center}
.phone-num{font-weight:600;font-size:18px;color:var(--ink)}
.field{position:absolute;left:125px;width:463px;height:39px;background:#fff;font-size:10.5px;color:#9a9394;padding:14px 18px}
.map{position:absolute;left:612px;top:1847px;width:463px;height:283px;background:linear-gradient(150deg,#e6e9e8 0%,#dfe5e2 50%,#e8eae6 100%)}

/* footer */
.footer{position:absolute;left:0;top:2220px;width:1200px;height:460px;background:var(--cream)}
.foot-head{position:absolute;top:2305px;font-family:"Marcellus",serif;font-size:16px;letter-spacing:1.5px;color:var(--rose);text-transform:uppercase}
.foot-links{position:absolute;top:2360px;list-style:none;font-size:9.5px;letter-spacing:2.2px;line-height:28.5px;text-transform:uppercase;color:var(--ink)}
.foot-rule{position:absolute;top:2275px;width:1px;height:275px;background:#efe2cd}
.foot-tag{position:absolute;left:600px;top:2440px;transform:translateX(-50%);font-size:11px;line-height:16px;color:var(--muted);text-align:center;width:340px}
.copyright{position:absolute;left:600px;top:2603px;transform:translateX(-50%);font-size:9px;line-height:15px;color:var(--muted);text-align:center;width:500px}
.to-top{position:absolute;left:1035px;top:2557px;width:80px;height:80px;border-radius:50%;background:#f3d9d6;display:flex;align-items:center;justify-content:center}
.to-top span{width:66px;height:66px;border-radius:50%;background:var(--rose);display:flex;align-items:center;justify-content:center}
</style>
</head>
<body>

<!-- header -->
<div class="nav-rule" style="left:83px;top:33px;width:410px"></div>
<div class="nav-rule" style="left:83px;top:91px;width:410px"></div>
<div class="nav-rule" style="left:707px;top:33px;width:410px"></div>
<div class="nav-rule" style="left:707px;top:91px;width:410px"></div>
<a class="nav-link is-active" style="left:142px">Home</a>
<a class="nav-link" style="left:273px">About</a>
<span class="nav-caret" style="left:273px"></span>
<a class="nav-link" style="left:417px">Services</a>
<span class="nav-caret" style="left:417px"></span>
<a class="nav-link" style="left:767px">Shop</a>
<a class="nav-link" style="left:900px">Testimonials</a>
<a class="nav-link" style="left:1045px">Contact</a>
<div class="brand" style="top:16px">
  <div class="brand-mark" style="width:52px;height:52px;margin-bottom:6px"></div>
  <div class="brand-name">Still Willow</div>
  <div class="brand-sub">Acupuncture</div>
</div>

<!-- hero -->
<div class="hero-photo" role="img" aria-label="Photo of acupuncture needles placed along a woman's neck and shoulder"></div>
<section class="philosophy">
  <h1>PHILOSOPHY OF CARE</h1>
  <p>Acupuncture &amp; Chinese Herbal Medicine are rooted in over 3000 years of history and tradition. As a complete medical system that has remained flexible and relevant we honor what has worked from the past while embracing the medicine of tomorrow.</p>
</section>
<a class="btn" style="left:465px;top:737px;width:270px">Schedule a consultation</a>

<!-- areas of focus -->
<div class="title-rule" style="left:338px;top:886px;width:64px"></div>
<h2 class="section-title" style="left:0;width:1200px;text-align:center;top:860px">AREAS OF FOCUS</h2>
<div class="title-rule" style="left:800px;top:886px;width:62px"></div>

<div class="focus-item" style="left:115px">
  <span class="focus-num">01</span>
  <div class="focus-disc"><div class="focus-art" role="img" aria-label="Illustration of a bird's nest with speckled eggs" style="background:radial-gradient(circle,#c8ccc8 0%,#c9a97e 55%,transparent 72%)"></div></div>
  <h3>Fertility<br>&amp; Pregnancy</h3>
  <p>At Still Willow Acupuncture our goal is to help build families and we happily embrace the diversity that word includes. We warmly welcome the LGBTQ community, single mothers and parents by choice and surrogates.</p>
</div>
<div class="focus-item" style="left:358px">
  <span class="focus-num">02</span>
  <div class="focus-disc"><div class="focus-art" role="img" aria-label="Illustration of stacked balancing stones" style="border-radius:40px;width:100px;background:linear-gradient(180deg,#f1e2de 0%,#b6bcb8 30%,#d6b3b1 55%,#2f4652 80%,transparent 90%)"></div></div>
  <h3>Hormone<br>Balance</h3>
  <p>Our hormones are constantly shifting and occasionally this internal orchestra needs to be refined. Acupuncture works to help the body rediscover the positive patterns that lead to improved health and well being.</p>
</div>
<div class="focus-item" style="left:602px">
  <span class="focus-num">03</span>
  <div class="focus-disc"><div class="focus-art" role="img" aria-label="Illustration of a leafy tree" style="background:radial-gradient(circle,#8d9088 0%,#b4b6b0 45%,transparent 70%)"></div></div>
  <h3>Strength and<br>Structure</h3>
  <p>Our bodies carry us through all we do. Sometimes they need attention and support. Whether you need a simple "tune up" or help recovering from surgery or illness acupuncture can help.</p>
</div>
<div class="focus-item" style="left:845px">
  <span class="focus-num">04</span>
  <div class="focus-disc"><div class="focus-art" role="img" aria-label="Illustration of a heart with radiating lines" style="background:radial-gradient(circle,#3f4a52 0%,#3f4a52 22%,#d9d9d9 30%,transparent 70%)"></div></div>
  <h3>Emotional<br>Wellbeing</h3>
  <p>Our mental and emotional wellness is imperative to whole body healing. Without the unity of heart and head other systems can suffer. Acupuncture and herbs can help reset patterns of relaxation while teaching the body to access these resources more easily on its' own.</p>
</div>

<a class="focus-go" style="left:215px" aria-label="Fertility and pregnancy"><svg width="12" height="12" viewBox="0 0 12 12"><path d="M4 2l4 4-4 4" fill="none" stroke="#fff" stroke-width="1.6"/></svg></a>
<a class="focus-go" style="left:458px" aria-label="Hormone balance"><svg width="12" height="12" viewBox="0 0 12 12"><path d="M4 2l4 4-4 4" fill="none" stroke="#fff" stroke-width="1.6"/></svg></a>
<a class="focus-go" style="left:702px" aria-label="Strength and structure"><svg width="12" height="12" viewBox="0 0 12 12"><path d="M4 2l4 4-4 4" fill="none" stroke="#fff" stroke-width="1.6"/></svg></a>
<a class="focus-go" style="left:945px" aria-label="Emotional wellbeing"><svg width="12" height="12" viewBox="0 0 12 12"><path d="M4 2l4 4-4 4" fill="none" stroke="#fff" stroke-width="1.6"/></svg></a>

<!-- contact -->
<section class="contact"></section>
<h2 class="section-title" style="left:125px;top:1678px">GET IN TOUCH</h2>
<div class="title-rule" style="left:448px;top:1703px;width:64px"></div>
<p class="contact-lead">An acupuncturist specializing in women's health, fertility challenges and pregnancy care in Fairhollow MA.</p>
<div class="phone">
  <div class="phone-icon"><svg width="20" height="20" viewBox="0 0 24 24"><path d="M6.6 10.8a15 15 0 006.6 6.6l2.2-2.2c.3-.3.7-.4 1-.2 1.1.4 2.3.6 3.6.6.6 0 1 .4 1 1V20c0 .6-.4 1-1 1A17 17 0 013 4c0-.6.4-1 1-1h3.5c.6 0 1 .4 1 1 0 1.3.2 2.5.6 3.6.1.3 0 .7-.2 1z" fill="#fff"/></svg></div>
  <span class="phone-num">413-555-0148</span>
</div>
<div class="field" style="top:1847px">Name</div>
<div class="field" style="top:1891px">Email</div>
<div class="field" style="top:1935px">Subject</div>
<div class="field" style="top:1979px;height:151px">Message</div>
<svg class="abs" style="left:548px;top:2090px" width="26" height="24" viewBox="0 0 26 24"><path d="M1 11L25 1 19 23 12 15z M12 15L25 1" fill="none" stroke="#b88a8f" stroke-width="1.6" stroke-linejoin="round"/></svg>
<div class="map" role="img" aria-label="Street map of the town showing the clinic location"></div>

<!-- footer -->
<footer class="footer"></footer>
<div class="foot-head" style="left:167px">Quick Links</div>
<ul class="foot-links" style="left:120px;width:160px;text-align:right">
  <li>Home</li><li>About</li><li>Services</li><li>Shop</li><li>Testimonials</li><li>Contact</li>
</ul>
<div class="foot-rule" style="left:363px"></div>
<div class="foot-rule" style="left:835px"></div>
<div class="brand" style="top:2274px">
  <div class="brand-mark" style="width:84px;height:84px;margin-bottom:14px"></div>
  <div class="brand-name" style="font-size:33px">Still Willow</div>
  <div class="brand-sub" style="font-size:17px;margin-top:5px">Acupuncture</div>
</div>
<p class="foot-tag">Free 15 minute phone consultations always available to answer any questions you may have.</p>
<a class="btn" style="left:467px;top:2508px;width:268px">Schedule a consultation</a>
<div class="foot-head" style="left:922px">Services</div>
<ul class="foot-links" style="left:922px">
  <li>Fertility &amp; Pregnancy</li><li>Hormone Balance</li><li>Strength &amp; Structure</li><li>Emotional Wellbeing</li><li>Privacy Policy</li><li>Terms &amp; Co.</li>
</ul>
<p class="copyright">Copyright © 2020 Still Willow Acupuncture | 48 Alder Lane | Fairhollow MA.<br>413-555-0148. All Rights Reserved.</p>
<a class="to-top" aria-label="Back to top"><span><svg width="22" height="14" viewBox="0 0 22 14"><path d="M2 12L11 3l9 9" fill="none" stroke="#fff" stroke-width="2"/></svg></span></a>

</body>
</html>
```